Business Card for Web Design consulting firm

Business card designs for Web Design consulting firm

Target Market(s)

English speaking adults ages 30 - 60. Predominantly professional services eg. Doctor, Dentist

Industry/Entity Type

Consulting

Requirements
Must have
• Double sided card

```html
<!DOCTYPE html>
<html lang="en">
<head>
<meta charset="utf-8">
<title>Velunta Business Card</title>
<link rel="stylesheet" href="https://fonts.googleapis.com/css2?family=Crimson+Text:wght@400;700&display=swap">
<style>
  :root {
    --paper: #ffffff;
    --card-black: #000000;
    --card-orange: #f7991f;
    --ink-grey: #4d4d4d;
  }
  * { margin: 0; padding: 0; box-sizing: border-box; }
  html, body {
    width: 1200px;
    height: 881px;
    overflow: hidden;
    background: var(--paper);
  }
  .canvas {
    position: relative;
    width: 1200px;
    height: 881px;
    background: var(--paper);
    font-family: "Crimson Text", Georgia, serif;
  }
  .card {
    position: absolute;
    top: 48px;
    width: 442px;
    height: 736px;
    overflow: hidden;
  }
  .card--front { left: 98px; background: var(--card-black); }
  .card--back  { left: 590px; background: var(--card-orange); }

  .brand-square {
    position: absolute;
    left: 122px;
    top: 303px;
    width: 128px;
    height: 128px;
    background: var(--card-orange);
  }
  .brand-name {
    position: absolute;
    left: 299px;
    top: 368px;
    transform: translate(-50%, -50%) rotate(-90deg);
    white-space: nowrap;
    color: var(--ink-grey);
    font-size: 62px;
    font-weight: 400;
    letter-spacing: 0.2em;
    line-height: 1;
    padding-left: 0.2em;
  }

  .contact {
    position: absolute;
    left: 228px;
    top: 376px;
    transform: translate(-50%, -50%) rotate(-90deg);
    white-space: nowrap;
    text-align: center;
    color: var(--ink-grey);
    font-size: 23px;
    line-height: 33px;
    letter-spacing: 0.14em;
  }
  .contact__name {
    font-weight: 700;
    letter-spacing: 0.2em;
  }
</style>
</head>
<body>
  <main class="canvas">
    <section class="card card--front" aria-label="Card front">
      <div class="brand-square" aria-hidden="true"></div>
      <div class="brand-name">VELUNTA</div>
    </section>

    <section class="card card--back" aria-label="Card back">
      <div class="contact">
        <p class="contact__name">Your Name</p>
        <p class="contact__line">p (555) 555-5555</p>
        <p class="contact__line">f (555) 555-5555</p>
        <p class="contact__line">yourname@mailbox.com</p>
        <p class="contact__line">www.yoursite.com</p>
      </div>
    </section>
  </main>
</body>
</html>
```